Commercial HVAC and Refrigeration Business cards

Frost-Haven Company is looking for flashy new business cards! We design, install, service and maintain commercial refrigeration, air conditioning, heating and refrigeration equipment. Our colors are blue and white. I'm open to single and double sided designs. Each employee will have their own business card. I've attached a copy of our current logo.

Our website, office and cell phone (cell phone is optional), email address should be clearly legible. "24 Hour Service" and the services we offer are; Sales, Service, Design, Installation, Maintenance. Refrigeration, Heating, Air Conditioning, Ice Machines. Does not have to be in any order.

Target Market(s)

Commercial; Restaurants, hotels, bars, breweries etc.

Industry/Entity Type

Hvac

Contact Information for Business Card

Name; Job Title, Phone Number, Email Address. www.frost-haven-example.com 24 Hour Service. We provide - Sales, Design, Installation, Service, Maintenance. We service - Refrigeration, Heating, Air Conditioning, Ice Machines

Font styles to use
Other font styles liked:
• Be creative

Colors
0255a3
ffffff

Requirements
Must have
• Professional appearance and appeal to commercial clients in the food-service and hospitality industry. Must be clearly legible and easy to understand.
Nice to have
• We want to sell maintenance agreements, perhaps we can use the back of the card to tie into a webpage about our maintenance agreements.
Should not have
• Cartoons or unprofessional. Nothing too edgy.

```html
<!DOCTYPE html>
<html lang="en">
<head>
<meta charset="utf-8">
<title>Frost-Haven Company – Business Cards</title>
<link href="https://fonts.googleapis.com/css2?family=Arimo:wght@400;700&display=swap" rel="stylesheet">
<style>
  :root {
    --brand-blue: #0255a3;
    --brand-white: #ffffff;
    --ink-grey: #555a60;
    --backdrop: #e9ecef;
  }
  * { box-sizing: border-box; margin: 0; padding: 0; }
  html, body { width: 1200px; height: 950px; overflow: hidden; }
  body {
    background: var(--backdrop);
    font-family: "Arimo", Arial, sans-serif;
    position: relative;
  }
  .card {
    position: absolute;
    width: 640px;
    height: 366px;
    box-shadow: 0 8px 24px rgba(0,0,0,0.18);
  }
  .card-frame { position: absolute; inset: 0; width: 100%; height: 100%; }
  .card-front { left: 80px; top: 80px; background: var(--brand-white); color: var(--brand-blue); }
  .card-back { left: 480px; top: 500px; background: var(--brand-blue); color: var(--brand-white); }

  .brand-name {
    position: absolute; left: 0; right: 0;
    text-align: center;
    font-weight: 700;
    font-size: 38px;
    letter-spacing: 0.5px;
  }
  .card-front .brand-name { top: 62px; color: var(--brand-blue); }
  .card-back .brand-name { top: 66px; color: var(--brand-white); }

  .agreements-title {
    position: absolute; left: 60px; right: 60px; top: 150px;
    text-align: center; font-weight: 700; font-size: 19px;
    color: var(--brand-blue);
    display: flex; align-items: center; gap: 14px;
  }
  .rule { flex: 1; height: 1px; background: var(--brand-blue); }
  .service-list {
    position: absolute; left: 58px; right: 40px; top: 200px;
    font-size: 16px; color: var(--ink-grey); line-height: 28px;
  }
  .service-list .label { font-size: 18px; display: inline-block; width: 110px; }

  .person-line {
    position: absolute; left: 60px; right: 60px; top: 150px;
    display: flex; align-items: center; gap: 14px; justify-content: center;
  }
  .person-line .rule { background: var(--brand-white); }
  .person-name { font-weight: 700; font-size: 20px; }
  .person-title { font-size: 15px; }
  .contact-row {
    position: absolute; left: 0; right: 0;
    display: flex; justify-content: center; gap: 22px;
    font-size: 16px;
  }
  .contact-row.primary { top: 200px; }
  .contact-row.web { top: 230px; }
  .contact-item { display: flex; align-items: center; gap: 6px; }
  .contact-item svg { width: 16px; height: 16px; fill: var(--brand-white); }
  .service-hours {
    position: absolute; left: 0; right: 0; top: 278px;
    text-align: center; font-size: 17px;
  }
</style>
</head>
<body>

<section class="card card-front" aria-label="Business card front">
  <svg class="card-frame" viewBox="0 0 640 366" aria-hidden="true">
    <path d="M42,20 H598 A22 22 0 0 0 620,42 V324 A22 22 0 0 0 598,346 H42 A22 22 0 0 0 20,324 V42 A22 22 0 0 0 42,20 Z"
          fill="none" stroke="var(--brand-blue)" stroke-width="3"/>
  </svg>
  <div class="brand-name">Frost-Haven Company</div>
  <div class="agreements-title"><span class="rule"></span>Maintenance agreements<span class="rule"></span></div>
  <div class="service-list">
    <p><span class="label">We provide :</span> Sales | Design | Installation | Service | Maintenance</p>
    <p><span class="label">We service :</span> Refrigeration | Heating | Air Conditioning | Ice Machines</p>
  </div>
</section>

<section class="card card-back" aria-label="Business card back">
  <svg class="card-frame" viewBox="0 0 640 366" aria-hidden="true">
    <path d="M42,20 H598 A22 22 0 0 0 620,42 V324 A22 22 0 0 0 598,346 H42 A22 22 0 0 0 20,324 V42 A22 22 0 0 0 42,20 Z"
          fill="none" stroke="var(--brand-white)" stroke-width="3"/>
  </svg>
  <div class="brand-name">Frost-Haven Company</div>
  <div class="person-line">
    <span class="rule"></span>
    <span class="person-name">Mark Ellison</span><span class="person-title">- President</span>
    <span class="rule"></span>
  </div>
  <div class="contact-row primary">
    <span class="contact-item">
      <svg viewBox="0 0 16 16" aria-hidden="true"><path d="M4 1 L6.5 1 L7.5 5 L5.8 6.2 Q7 9.5 9.8 10.2 L11 8.5 L15 9.5 L15 12 Q14 15 11 15 Q2 13 1 4 Q1 1 4 1 Z"/></svg>
      555 010 2468
    </span>
    <span class="contact-item">
      <svg viewBox="0 0 16 16" aria-hidden="true"><path d="M1 3 H15 V13 H1 Z M2 4 L8 9 L14 4 Z" fill-rule="evenodd"/></svg>
      mark@frost-haven-example.com
    </span>
  </div>
  <div class="contact-row web">
    <span class="contact-item">
      <svg viewBox="0 0 16 16" aria-hidden="true"><circle cx="8" cy="8" r="7"/><path d="M1 8 H15 M8 1 Q4 8 8 15 M8 1 Q12 8 8 15" stroke="var(--brand-blue)" stroke-width="1.2" fill="none"/></svg>
      www.frost-haven-example.com
    </span>
  </div>
  <div class="service-hours">24 Hour Service.</div>
</section>

</body>
</html>
```